Catalog copying current designs, web designs and copywrite.

I am looking for someone to recreate a draft catalog using the same design process.

My entire brief with the photo samples and icons would not fit in here. They are in the google docs folder as below:

https://files.brindlecove.net/share/folders/7qXk2mPz9LwRt4VhYs3NcB0aJdE6uFgHo?mode=viewer

```html
<!DOCTYPE html>
<html lang="en">
<head>
<meta charset="utf-8">
<title>Ironbark Labour Hire Solutions – Catalogue Spreads</title>
<link href="https://fonts.googleapis.com/css2?family=Archivo+Black&family=Arimo:ital,wght@0,400;0,700;1,400;1,700&display=swap" rel="stylesheet">
<style>
  :root{
    --red:#b01c22;
    --crimson:#8e141a;
    --wine:#6f0f14;
    --deep:#550a0e;
    --paper:#e6e6e6;
    --paper-dark:#d3d3d3;
    --ink:#262626;
    --body:#4a4a4a;
    --muted:#b9b9b9;
    --white:#ffffff;
  }
  *{box-sizing:border-box;margin:0;padding:0}
  html,body{width:714px;height:1200px;overflow:hidden;background:#fff}
  body{font-family:"Arimo",Arial,sans-serif;color:var(--ink)}
  .sheet{position:relative;width:714px;height:1200px;background:#fff;overflow:hidden}

  .page{position:absolute;width:190px;height:268px;overflow:hidden;
    background:linear-gradient(155deg,#efefef 0%,var(--paper) 45%,var(--paper-dark) 100%)}
  .col-1{left:32px}.col-2{left:262px}.col-3{left:492px}
  .row-1{top:34px}.row-2{top:323px}.row-3{top:612px}.row-4{top:900px}

  .backdrop{position:absolute;inset:0;background:linear-gradient(160deg,var(--crimson) 0%,var(--wine) 55%,var(--deep) 100%)}
  .photo{position:absolute;inset:0;background:linear-gradient(165deg,#de7a7c 0%,#b8353a 55%,#871a1f 100%)}
  .photo.dark{background:linear-gradient(170deg,#c75a5d 0%,#9b2227 50%,#5e0d12 100%)}

  .abs{position:absolute}
  .vtitle{position:absolute;left:9px;top:12px;writing-mode:vertical-rl;transform:rotate(180deg);
    font-weight:700;font-size:15px;letter-spacing:-.3px;color:var(--muted);line-height:1;white-space:nowrap}
  .body{font-size:3.2px;line-height:1.35;color:var(--body);text-align:justify}
  .body.center{text-align:center}
  .body.light{color:#f3dcdc}
  .red{color:var(--red)}
  .label{font-size:3.4px;font-weight:700;text-transform:uppercase;text-align:center;line-height:1.2}
  .url{position:absolute;right:12px;bottom:8px;font-size:5.2px;color:var(--white)}

  .brand{position:absolute;display:flex;align-items:center;gap:3px}
  .brand-mark{width:7px;height:7px;background:var(--ink)}
  .brand-name{font-weight:700;font-size:15px;color:var(--red);letter-spacing:-.3px;line-height:1}
  .brand-tag{position:absolute;font-size:3.2px;letter-spacing:1.8px;font-weight:700;color:var(--ink)}
  .brand.reverse .brand-mark{background:var(--white)}
  .brand.reverse .brand-name{color:var(--white)}
  .brand-tag.reverse{color:var(--white)}

  .step-num{position:absolute;left:50px;font-family:"Archivo Black",sans-serif;font-size:20px;color:var(--red);line-height:1}
  .step-head{position:absolute;left:78px;font-weight:700;font-size:8px;color:var(--red)}
  .step-copy{position:absolute;left:78px;width:100px}

  .about-kicker{font-weight:700;font-size:8px;color:var(--red)}
  .about-head{font-family:"Archivo Black",sans-serif;font-size:12.6px;line-height:1.15;color:var(--ink)}
  .value-icon{position:absolute;width:20px;height:20px;border-radius:50%;background:var(--red);display:flex;align-items:center;justify-content:center}
  .value-label{position:absolute;width:52px;font-size:3.4px;text-align:center;color:var(--ink)}

  .insight-kicker{font-weight:700;font-size:8px;color:var(--red)}
  .insight-head{font-family:"Archivo Black",sans-serif;font-size:17px;line-height:1.05;color:var(--ink)}
  .stat{position:absolute;left:108px;display:flex;align-items:center;gap:4px}
  .stat-num{width:20px;height:20px;border-radius:50%;background:#3a3a3a;border:1.4px solid var(--red);color:#fff;font-weight:700;font-size:7px;display:flex;align-items:center;justify-content:center}
  .stat-label{font-size:5px;font-weight:700;color:var(--red)}

  .svc{position:absolute;width:54px;text-align:center}
  .svc svg{display:block;margin:0 auto 2px}
  .svc .label{color:var(--red);margin-bottom:2px}
  .svc.on-red .label{color:#fff}

  .feature{position:absolute;text-align:center}
  .feature .disc{width:16px;height:16px;border-radius:50%;background:var(--red);margin:0 auto 2px;display:flex;align-items:center;justify-content:center}
  .feature .label{font-size:3px;color:var(--ink);margin-bottom:1px}
  .feature .body{font-size:2.7px}
  .need-band{position:absolute;left:0;top:123px;width:190px;height:63px;background:var(--wine)}
  .need-title{position:absolute;top:5px;width:100%;text-align:center;font-weight:700;font-size:8.6px;color:#fff}
  .need-sub{position:absolute;top:17px;left:10px;right:10px;font-size:3px;text-align:center;color:#f3dcdc;line-height:1.3}
  .need-steps{position:absolute;top:27px;left:8px;right:8px;display:grid;grid-template-columns:repeat(6,1fr);text-align:center;color:#fff}
  .need-steps b{display:block;font-family:"Archivo Black",sans-serif;font-size:13px;line-height:1}
  .need-steps span{display:block;font-size:2.7px;line-height:1.25;margin-top:1px}
  .roles{position:absolute;left:6px;right:6px;display:grid;grid-template-columns:repeat(6,1fr);row-gap:4px;text-align:center}
  .pictogram{margin:0 auto 1px;border-radius:40% 40% 20% 20%;
    background:radial-gradient(circle at 50% 35%,var(--red) 0%,rgba(176,28,34,.55) 45%,rgba(176,28,34,0) 72%)}
  .roles .pictogram{width:15px;height:16px}
  .role-name{font-size:2.7px;font-weight:700;color:var(--ink);text-transform:uppercase;line-height:1.2}

  .wu-head{font-weight:700;font-size:7.8px;line-height:1.15;color:var(--red);letter-spacing:.2px}
  .wu-sub{font-weight:700;font-size:5.4px;line-height:1.2;color:var(--red)}
  .wu-list{list-style:none;font-size:3.05px;line-height:1.35;color:var(--body)}
  .wu-list li{padding-left:3px;text-indent:-3px}
  .wu-list li::before{content:"• "}
  .wu-icon{position:absolute;left:12px;width:24px;height:24px;border-radius:50%;
    background:radial-gradient(circle,rgba(176,28,34,.5) 0%,rgba(176,28,34,.15) 60%,rgba(176,28,34,0) 72%)}

  .rec-title{font-weight:700;font-size:8.8px;color:#fff}
  .rec-steps{position:absolute;left:58px;width:100px;display:grid;grid-template-columns:repeat(3,1fr);text-align:center;color:#fff}
  .rec-steps b{display:block;font-family:"Archivo Black",sans-serif;font-size:14px;line-height:1}
  .rec-steps span{display:block;font-size:3px;line-height:1.25;margin-top:1px}
  .pos-title{font-weight:700;font-size:9px;color:var(--ink);text-align:center}
  .positions{position:absolute;left:32px;width:140px;display:grid;grid-template-columns:repeat(4,1fr);text-align:center}
  .positions .pictogram{width:18px;height:21px}
  .pos-name{font-size:2.8px;font-weight:700;color:var(--ink);text-transform:uppercase;line-height:1.2;height:7px}

  .client{position:absolute;width:74px;text-align:center;font-weight:700;color:#575757;line-height:1.05}

  .proj{position:absolute;width:34px}
  .proj-img{height:28px;background:linear-gradient(170deg,#9fb2c4 0%,#c9b49c 55%,#6e5a4a 100%)}
  .proj-cap{background:#fff;font-size:2.5px;line-height:1.15;text-align:center;color:var(--ink);padding:.5px 1px;height:7px}

  .contact-lead{position:absolute;right:12px;width:120px;text-align:right;font-size:4.3px;line-height:1.35;color:var(--ink)}
  .contact-lead.em{font-style:italic;font-weight:700;color:var(--red)}
  .contact-row{position:absolute;right:12px;display:flex;align-items:center;gap:3px;font-size:4.3px;font-weight:700;color:var(--ink)}
  .contact-row .dot{width:9px;height:9px;border-radius:50%;background:var(--red);display:flex;align-items:center;justify-content:center}
</style>
</head>
<body>
<main class="sheet">

  <!-- Cover -->
  <section class="page col-1 row-1">
    <div class="photo" role="img" aria-label="Red-toned photo of a site worker in a company shirt standing beside a tower crane above the city" style="clip-path:polygon(70px 0,190px 0,190px 168px,125px 152px,70px 165px,0 150px,0 118px,35px 112px,70px 100px)"></div>
    <div class="backdrop" role="img" aria-label="Deep red low-poly backdrop" style="clip-path:polygon(0 150px,70px 165px,125px 152px,190px 168px,190px 268px,0 268px)"></div>
    <div class="brand" style="left:13px;top:18px"><span class="brand-mark"></span><span class="brand-name">ironbark</span></div>
    <div class="brand-tag" style="left:23px;top:36px">LABOUR HIRE SOLUTIONS</div>
    <div class="url">www.ironbarklabour.com.au</div>
  </section>

  <!-- Why us -->
  <section class="page col-2 row-1">
    <div class="photo" role="img" aria-label="Red-toned photo of a worker in a hard hat handling heavy chains on site" style="clip-path:polygon(0 104px,28px 100px,55px 128px,90px 150px,130px 165px,165px 163px,190px 188px,190px 268px,0 268px)"></div>
    <div class="vtitle">WHY US?</div>
    <div class="step-num" style="top:31px">1</div>
    <div class="step-head" style="top:33px">INITIATION</div>
    <p class="step-copy body" style="top:46px">Ironbark initially engages with the employer to create a business relationship. We understand the clients' needs and assign appropriate measures to forward our services.</p>
    <div class="step-num" style="top:69px">2</div>
    <div class="step-head" style="top:71px">ASSESSMENT</div>
    <p class="step-copy body" style="top:84px">We assess the employers' criteria and hand over the appropriate candidates for their job. Unlike most recruitment companies, we do not bulk-send a bunch of resumes, but rather ensure that we are sending the greatest quality candidates that best meet their needs.</p>
    <div class="step-num" style="top:117px">3</div>
    <div class="step-head" style="top:119px">PLACEMENT</div>
    <p class="step-copy body" style="top:132px">Employers then interview the candidate put forward by Ironbark in order to fill the vacancy and ensure that the candidate is the best fit for their position.</p>
  </section>

  <!-- About us -->
  <section class="page col-3 row-1">
    <div class="vtitle">ABOUT US</div>
    <div class="abs about-kicker" style="left:12px;top:114px">INDUSTRY LEADING</div>
    <div class="abs about-head" style="left:12px;top:124px">RECRUITMENT &amp;<br>LABOUR HIRE AGENCY</div>
    <div class="abs about-kicker" style="right:12px;top:155px">IN NEW SOUTH WALES</div>
    <p class="abs body" style="left:12px;top:177px;width:80px">At Ironbark, we're all about ensuring our clients achieve their goals and succeed in their field. This is why so many construction companies have trusted us in providing qualified workers for their projects. Make an enquiry and watch these words be put into action.</p>
    <p class="abs body" style="left:98px;top:177px;width:80px">We are extremely passionate about what we do, excellence in the Labour Hire industry has become second nature for us. We work to give you many reasons to engage with Ironbark services. We have become a well renowned Recruitment &amp; Labour Hire company by upholding the following values:</p>
    <div class="value-icon" style="left:33px;top:219px"><svg width="10" height="10" viewBox="0 0 10 10"><circle cx="5" cy="4" r="2.6" fill="none" stroke="#fff" stroke-width=".7"/><path d="M4 7.2h2M4.3 8.4h1.4" stroke="#fff" stroke-width=".7"/></svg></div>
    <div class="value-icon" style="left:85px;top:219px"><svg width="10" height="10" viewBox="0 0 10 10"><circle cx="5" cy="5" r="3.8" fill="none" stroke="#fff" stroke-width=".7"/><circle cx="5" cy="5" r="2.2" fill="none" stroke="#fff" stroke-width=".7"/><circle cx="5" cy="5" r=".7" fill="#fff"/></svg></div>
    <div class="value-icon" style="left:137px;top:219px"><svg width="10" height="10" viewBox="0 0 10 10"><path d="M1.5 5.2l2.3 2.3 4.7-5" fill="none" stroke="#fff" stroke-width=".9"/></svg></div>
    <div class="value-label" style="left:17px;top:245px">INSPIRING OTHERS</div>
    <div class="value-label" style="left:69px;top:245px">ACHIEVING GOALS</div>
    <div class="value-label" style="left:121px;top:245px">WORKING TO SUCCEED</div>
  </section>

  <!-- Insight -->
  <section class="page col-1 row-2">
    <div class="photo" role="img" aria-label="Red-toned photo of an operator seated in the cab of heavy machinery on a building site" style="clip-path:polygon(0 0,190px 0,190px 108px,160px 96px,120px 98px,70px 80px,30px 57px,0 62px)"></div>
    <div class="abs insight-kicker" style="left:12px;top:111px">A BIT OF</div>
    <div class="abs insight-head" style="left:12px;top:121px">AN<br>INSIGHT</div>
    <p class="abs body" style="left:12px;top:174px;width:93px">We are an industry leading permanent recruitment and labour hire company who pride ourselves on having the highest of quality workers whilst maintaining greatest efficiency possible for clients. We are no strangers to the industries we serve and possess extensive experience and knowledge in our field.</p>
    <p class="abs body" style="left:12px;top:210px;width:93px">Our mission is simple – to leave a profound service of excellence in the construction industry without the exorbitant staffing costs for client requirements. We achieve this outcome through stringent screening processes in aim of engaging only the most experienced candidates for our clients. We deliver highly competitive pricing through maintaining low overheads and efficient processes in place to ensure your project budgets are met.</p>
    <div class="stat" style="top:142px"><span class="stat-num">37</span><span class="stat-label">Satisfied Clients</span></div>
    <div class="stat" style="top:174px"><span class="stat-num">316</span><span class="stat-label">Employees</span></div>
    <div class="stat" style="top:205px"><span class="stat-num">68</span><span class="stat-label">Jobsites</span></div>
    <div class="stat" style="top:237px"><span class="stat-num">8</span><span class="stat-label">Staff Members</span></div>
  </section>

  <!-- Our services -->
  <section class="page col-2 row-2">
    <div class="backdrop" role="img" aria-label="Deep red low-poly backdrop" style="clip-path:polygon(0 162px,70px 150px,100px 152px,135px 185px,160px 175px,190px 165px,190px 268px,0 268px)"></div>
    <div class="vtitle">OUR SERVICES</div>
    <div class="svc" style="left:44px;top:12px">
      <svg width="20" height="18" viewBox="0 0 20 18" fill="none" stroke="#333" stroke-width=".8"><rect x="2" y="8" width="16" height="8"/><path d="M2 12h16M7 8v8M13 8v8M5 8V4h10v4"/></svg>
      <div class="label">LABOUR HIRE</div>
      <p class="body">Lorem ipsum dolor sit amet, consectetuer adipiscing elit, sed diam nonummy nibh euismod tincidunt ut laoreet</p>
    </div>
    <div class="svc" style="left:111px;top:27px">
      <svg width="20" height="18" viewBox="0 0 20 18" fill="none" stroke="#333" stroke-width=".8"><path d="M5 17V2h12M5 4l4-2M15 2v7M12 12h6v4h-6z"/></svg>
      <div class="label">CRANE SUPPLY</div>
      <p class="body">Lorem ipsum dolor sit amet, consectetuer adipiscing elit, sed diam nonummy nibh euismod tincidunt ut laoreet</p>
    </div>
    <div class="svc" style="left:44px;top:82px">
      <svg width="20" height="18" viewBox="0 0 20 18" fill="none" stroke="#333" stroke-width=".8"><path d="M3 17V2h14v15M6 17V5h8v12M3 2l3 3M17 2l-3 3"/></svg>
      <div class="label">RIGGING</div>
      <p class="body">Lorem ipsum dolor sit amet, consectetuer adipiscing elit, sed diam nonummy nibh euismod tincidunt ut laoreet</p>
    </div>
    <div class="svc" style="left:111px;top:97px">
      <svg width="20" height="18" viewBox="0 0 20 18" fill="none" stroke="#333" stroke-width=".8"><path d="M10 1l5 14H5zM7 9h6M8 5h4M2 17h16"/></svg>
      <div class="label">TRAFFIC CONTROL</div>
      <p class="body">Lorem ipsum dolor sit amet, consectetuer adipiscing elit, sed diam nonummy nibh euismod tincidunt ut laoreet</p>
    </div>
    <div class="svc on-red" style="left:12px;top:175px">
      <svg width="18" height="20" viewBox="0 0 18 20" fill="none" stroke="#fff" stroke-width=".8"><rect x="2" y="1" width="14" height="18"/><path d="M9 1v18M4 4h3v7H4zM11 4h3v7h-3z"/></svg>
      <div class="label">COMMERCIAL<br>CLEANING</div>
      <p class="body light">Lorem ipsum dolor sit amet, consectetuer adipiscing elit, sed diam nonummy nibh euismod tincidunt ut laoreet</p>
    </div>
    <div class="svc on-red" style="left:68px;top:186px">
      <svg width="20" height="18" viewBox="0 0 20 18" fill="none" stroke="#fff" stroke-width=".8"><rect x="2" y="1" width="12" height="12"/><rect x="7" y="6" width="11" height="11"/><path d="M8 1v12M2 7h12"/></svg>
      <div class="label">TILING<br>(SUPPLY &amp; INSTALL)</div>
      <p class="body light">Lorem ipsum dolor sit amet, consectetuer adipiscing elit, sed diam nonummy nibh euismod tincidunt ut laoreet</p>
    </div>
    <div class="svc on-red" style="left:126px;top:196px">
      <svg width="20" height="18" viewBox="0 0 20 18" fill="none" stroke="#fff" stroke-width=".8"><path d="M3 12h14v3H3zM6 12V7h6v5M12 8l4-6 3 4"/><circle cx="6" cy="16" r="1"/><circle cx="14" cy="16" r="1"/></svg>
      <div class="label">MACHINE<br>HIRE</div>
      <p class="body light">Lorem ipsum dolor sit amet, consectetuer adipiscing elit, sed diam nonummy nibh euismod tincidunt ut laoreet</p>
    </div>
  </section>

  <!-- Labour hire -->
  <section class="page col-3 row-2">
    <div class="vtitle">LABOUR HIRE</div>
    <div class="feature" style="left:40px;top:12px;width:62px">
      <div class="disc"><svg width="8" height="8" viewBox="0 0 8 8" fill="none" stroke="#fff" stroke-width=".6"><path d="M1 1h6v4H3L1 7z"/></svg></div>
      <div class="label">COMMUNICATION</div>
      <p class="body">We believe communication is a significant part of a successful business relationship which is why our communication is impeccable. We are contactable 24 hours a day, 7 days a week.</p>
    </div>
    <div class="feature" style="left:105px;top:12px;width:62px">
      <div class="disc"><svg width="8" height="8" viewBox="0 0 8 8" fill="none" stroke="#fff" stroke-width=".6"><circle cx="4" cy="4.4" r="3"/><path d="M4 2.6v1.8l1.2.8M3 .6h2"/></svg></div>
      <div class="label">FAST SERVICE</div>
      <p class="body">We understand the timing of construction, which is why we work as quick as possible, so you don't have to worry. We can work on even a days' notice and have workers ready to start!</p>
    </div>
    <div class="feature" style="left:31px;top:58px;width:46px">
      <div class="disc"><svg width="8" height="8" viewBox="0 0 8 8" fill="#fff"><circle cx="2" cy="3" r="1"/><circle cx="4" cy="2.4" r="1.1"/><circle cx="6" cy="3" r="1"/><rect x="1" y="4.6" width="6" height="2" rx=".8"/></svg></div>
      <div class="label">EXPERTS IN OUR FIELD</div>
      <p class="body">All our consultants have extensive experience in the building &amp; construction and associated industries, so you can be confident that each consultant you speak to understands the finer details of the arrangement.</p>
    </div>
    <div class="feature" style="left:80px;top:58px;width:46px">
      <div class="disc"><svg width="8" height="8" viewBox="0 0 8 8" fill="none" stroke="#fff" stroke-width=".6"><path d="M1 4l3-3h3v3L4 7z"/><circle cx="5.5" cy="2.5" r=".5" fill="#fff"/></svg></div>
      <div class="label">PRICE COMPETITIVE</div>
      <p class="body">We know the accolades of labour hire companies out there, and sometimes it can be difficult choosing the right one, which is why we have made it easy for you by having the best rates in NSW guaranteed.</p>
    </div>
    <div class="feature" style="left:130px;top:58px;width:46px">
      <div class="disc"><svg width="8" height="8" viewBox="0 0 8 8" fill="none" stroke="#fff" stroke-width=".6"><path d="M4 1l.9 2 2.1.2-1.6 1.4.5 2.1L4 5.6 2.1 6.7l.5-2.1L1 3.2 3.1 3z"/></svg></div>
      <div class="label">OUR WORKERS</div>
      <p class="body">We can confidently say we have one of the best teams in NSW. All of our workers have had a world of experience in each of their roles. So you can be confident your site will be handled professionally and delivered with quality.</p>
    </div>
    <div class="need-band">
      <div class="need-title">WHY DO I NEED LABOUR HIRE?</div>
      <p class="need-sub">This is the first step to realising why you need Labour Hire. We've got the guys you're looking for, we just need to get to know you a bit better and here's how we get the ball rolling.</p>
      <div class="need-steps">
        <div><b>1</b><span>Assess what workers you need</span></div>
        <div><b>2</b><span>Understand which projects you need help on</span></div>
        <div><b>3</b><span>Finding out when you need these workers to start</span></div>
        <div><b>4</b><span>Knowing how long you need these workers for</span></div>
        <div><b>5</b><span>Getting our workers starting up and ready!</span></div>
        <div><b>6</b><span>Start cutting costs and ensure your projects runs smoothly</span></div>
      </div>
    </div>
    <div class="roles" style="top:193px">
      <div><div class="pictogram" role="img" aria-label="Red pictogram of a crane operator"></div><div class="role-name">Crane<br>Operator</div></div>
      <div><div class="pictogram" role="img" aria-label="Red pictogram of a dogman"></div><div class="role-name">Dogman</div></div>
      <div><div class="pictogram" role="img" aria-label="Red pictogram of a rigger"></div><div class="role-name">Rigger</div></div>
      <div><div class="pictogram" role="img" aria-label="Red pictogram of a carpenter"></div><div class="role-name">Carpenter</div></div>
      <div><div class="pictogram" role="img" aria-label="Red pictogram of a boilermaker"></div><div class="role-name">Boilermaker</div></div>
      <div><div class="pictogram" role="img" aria-label="Red pictogram of a welder"></div><div class="role-name">Welder</div></div>
      <div><div class="pictogram" role="img" aria-label="Red pictogram of an excavator operator"></div><div class="role-name">Excavator<br>Operator</div></div>
      <div><div class="pictogram" role="img" aria-label="Red pictogram of an elevated work platform"></div><div class="role-name">EWP</div></div>
      <div><div class="pictogram" role="img" aria-label="Red pictogram of a general labourer"></div><div class="role-name">General<br>Labourer</div></div>
      <div><div class="pictogram" role="img" aria-label="Red pictogram of a skilled labourer"></div><div class="role-name">Skilled<br>Labourer</div></div>
      <div><div class="pictogram" role="img" aria-label="Red pictogram of a traffic controller"></div><div class="role-name">Traffic<br>Controller</div></div>
      <div><div class="pictogram" role="img" aria-label="Red pictogram of a scaffolder"></div><div class="role-name">Scaffolder</div></div>
    </div>
  </section>

  <!-- Why use a labour hire company -->
  <section class="page col-1 row-3">
    <div class="abs wu-head" style="left:12px;top:11px;width:168px">WHY USE A LABOUR HIRE COMPANY WITHIN CONSTRUCTION?</div>
    <p class="abs body" style="left:12px;top:32px;width:168px;font-size:3.05px">With all industries, particularly the construction industry and related sectors, there are certain stigmas that tend to be attached with the concept of labour hire, these stigmas potentially stem from bad experiences, hearsay or just inexperience in engaging with labour hire companies. The concept of "spending too much money on labour hire companies", can make it quite daunting and potentially cause companies to become overly focused on the expenses associated in the process. If this was the case, the word "investment" would arguably become nullified. In practical terms, engaging in labour hire services vs sourcing candidates internally can appear to be costly. However much like any investment, the consideration of other factors is imperative to the success of any process.</p>
    <div class="abs wu-sub" style="left:12px;top:81px;width:160px">SOME OF THE KEY ADVANTAGES OF ENGAGING WITH LABOUR HIRE INCLUDE:</div>
    <ul class="abs wu-list" style="left:12px;top:98px;width:168px">
      <li>Eliminating the time consuming and lengthy procedures in finding the right candidate.</li>
      <li>Ensuring the quality of candidates by pre-screening and reference checking.</li>
      <li>Candidates engaged through labour hire come with additional skills and expertise that may otherwise be absent among in-house employees.</li>
      <li>Flexibility of engagement terms, there is a very minimal commitment to available work provided to the Candidate.</li>
      <li>Reduction and potential elimination of some procedures and processes relating to WHS, RTW, and insurance costs.</li>
      <li>Efficient and effective systems ensuring an immediate supply of personnel.</li>
      <li>Simplification and elimination of payroll procedures and processes.</li>
    </ul>
    <div class="wu-icon" style="top:149px" role="img" aria-label="Red line illustration of a hand holding coins and a clock"></div>
    <p class="abs body" style="left:43px;top:152px;width:137px">All the above-mentioned benefits of engaging in labour hire services are there to save the client time, heartache and ultimately reduce costs and still retain professional staffing services. All the client needs to focus on the delivery of the project.</p>
    <svg class="abs" style="left:12px;top:186px" width="24" height="22" viewBox="0 0 24 22" fill="none" stroke="var(--red)" stroke-width="1"><path d="M1 21h22"/><rect x="2" y="14" width="3" height="7"/><rect x="7" y="11" width="3" height="10"/><rect x="12" y="8" width="3" height="13"/><rect x="17" y="5" width="3" height="16"/><path d="M2 10l6-4 5 2 8-7M18 1h3v3"/></svg>
    <p class="abs body" style="left:43px;top:184px;width:137px">According to the <span class="red">National Workforce Data Office</span>, approximately 600,800 people (about 5%) of all people employed, found work through via a recruitment agency. From this figure it is evident that an increase in the confidence and engagement of recruitment agencies is on the rise and can truly be considered a value adding process for the related industries. Prediction of an annual growth of approximately 2.4%, indicates that the industry will continue to go from "strong" to "stronger" in the near future.</p>
    <div class="wu-icon" style="top:226px" role="img" aria-label="Red line illustration of a hand with a clock"></div>
    <p class="abs body" style="left:43px;top:230px;width:137px">In summary, you can be confident that price is only a minor factor of the greater picture when engaging labour hire services. Added-value factoring outweighs the negative stigma related to labour hire companies being overpriced. At Ironbark we offer a wide variety of services, if you are looking for a company to engage with for your staffing needs without the fuss, look no further, <span class="red">submit a vacancy</span> today.</p>
  </section>

  <!-- Permanent recruitment -->
  <section class="page col-2 row-3">
    <div class="backdrop" role="img" aria-label="Deep red low-poly backdrop" style="clip-path:polygon(0 0,190px 0,190px 120px,150px 116px,115px 110px,88px 125px,55px 120px,25px 140px,0 152px)"></div>
    <div class="vtitle" style="font-size:14.5px;color:rgba(205,205,205,.85)">PERMANENT RECRUITMENT</div>
    <div class="abs rec-title" style="left:35px;top:11px">OUR RECRUITMENT PROCESS</div>
    <p class="abs body center light" style="left:30px;top:28px;width:145px">Our job is to simplify difficulties of recruitment so you can focus on what you do best, it is vital to understand your needs so we can find you the newest addition to your team. Here's a snippet of our process.</p>
    <div class="rec-steps" style="top:54px">
      <div><b>1</b><span>Understanding what you want</span></div>
      <div><b>2</b><span>Screen through candidates</span></div>
      <div><b>3</b><span>Interview the most eligible candidates</span></div>
    </div>
    <div class="rec-steps" style="top:85px">
      <div><b>4</b><span>Perform reference checks</span></div>
      <div><b>5</b><span>Arrange interview</span></div>
      <div><b>6</b><span>Place the Candidate</span></div>
    </div>
    <div class="abs pos-title" style="left:30px;width:150px;top:145px">POSITIONS WE PROVIDE</div>
    <div class="abs" style="left:30px;width:150px;top:157px;font-size:3.2px;text-align:center;color:var(--body)">(BUT NOT LIMITED TO)</div>
    <div class="positions" style="top:166px">
      <div><div class="pictogram" role="img" aria-label="Red pictogram of a construction manager"></div><div class="pos-name">Construction Manager</div></div>
      <div><div class="pictogram" role="img" aria-label="Red pictogram of a project manager"></div><div class="pos-name">Project Manager</div></div>
      <div><div class="pictogram" role="img" aria-label="Red pictogram of a site manager"></div><div class="pos-name">Site Manager</div></div>
      <div><div class="pictogram" role="img" aria-label="Red pictogram of a foreman"></div><div class="pos-name">Foreman</div></div>
    </div>
    <div class="positions" style="top:205px">
      <div><div class="pictogram" role="img" aria-label="Red pictogram of an estimator"></div><div class="pos-name">Estimator</div></div>
      <div><div class="pictogram" role="img" aria-label="Red pictogram of a contracts administrator"></div><div class="pos-name">Contracts Administrator</div></div>
      <div><div class="pictogram" role="img" aria-label="Red pictogram of a leading hand"></div><div class="pos-name">Leading Hand</div></div>
      <div><div class="pictogram" role="img" aria-label="Red pictogram of a cadet"></div><div class="pos-name">Cadet</div></div>
    </div>
    <div class="abs" style="left:30px;width:150px;top:244px;font-size:3.4px;text-align:center;color:var(--body)">AND SO MUCH MORE…</div>
  </section>

  <!-- Our clients -->
  <section class="page col-3 row-3">
    <div class="vtitle">OUR CLIENTS</div>
    <div class="client" style="left:55px;top:14px;width:100px;font-size:6px">Harbourline</div>
    <div class="client" style="left:32px;top:32px;width:40px;font-size:6px">Corbel</div>
    <div class="client" style="left:70px;top:32px;width:40px;font-size:6px">Dunmore</div>
    <div class="client" style="left:113px;top:32px;width:50px;font-size:5px">Sentra C&amp;T</div>
    <div class="client" style="left:22px;top:61px;font-size:7.5px">Marrick</div>
    <div class="client" style="left:96px;top:60px;font-size:7.5px">Bolwarra</div>
    <div class="client" style="left:22px;top:92px;font-size:6px">Wide Field</div>
    <div class="client" style="left:96px;top:92px;font-size:6px">Tramline</div>
    <div class="client" style="left:96px;top:112px;font-size:7px">KD Cranes</div>
    <div class="client" style="left:22px;top:136px;font-size:5.5px">Broadreach</div>
    <div class="client" style="left:96px;top:133px;font-size:8px">Trident</div>
    <div class="client" style="left:22px;top:160px;font-size:9px">Nexford</div>
    <div class="client" style="left:96px;top:160px;font-size:9px">Alder</div>
    <div class="client" style="left:22px;top:186px;font-size:9px">Bindara</div>
    <div class="client" style="left:96px;top:184px;font-size:5.4px">Pinnacle Cranes &amp; Rigging</div>
    <div class="client" style="left:22px;top:212px;font-size:9px">Corbel</div>
    <div class="client" style="left:22px;top:238px;font-size:9px">Tier</div>
    <div class="client" style="left:96px;top:239px;font-size:7px">Westholm</div>
  </section>

  <!-- Projects -->
  <section class="page col-1 row-4">
    <div class="backdrop" role="img" aria-label="Deep red low-poly backdrop" style="clip-path:polygon(0 100px,30px 112px,70px 140px,110px 150px,150px 145px,190px 160px,190px 268px,0 268px)"></div>
    <div class="vtitle">PROJECTS</div>
    <div class="proj" style="left:31px;top:12px"><div class="proj-img" role="img" aria-label="Render of a mid-rise apartment building"></div><div class="proj-cap">12-18 Ridge Street, Alderton NSW</div></div>
    <div class="proj" style="left:69px;top:12px"><div class="proj-img" role="img" aria-label="Render of a brick apartment block"></div><div class="proj-cap">140-144 Fern Street, Kellmore NSW</div></div>
    <div class="proj" style="left:107px;top:12px"><div class="proj-img" role="img" aria-label="Render of a residential tower"></div><div class="proj-cap">52A Quarry St, Elmstead NSW</div></div>
    <div class="proj" style="left:145px;top:12px"><div class="proj-img" role="img" aria-label="Render of a white apartment building"></div><div class="proj-cap">10-16 Bay St, Coralton NSW</div></div>
    <div class="proj" style="left:31px;top:59px"><div class="proj-img" role="img" aria-label="Render of a corner mixed-use building"></div><div class="proj-cap">401-409 Hill Rd, Marrowby NSW</div></div>
    <div class="proj" style="left:69px;top:59px"><div class="proj-img" role="img" aria-label="Render of a tall apartment tower"></div><div class="proj-cap">22 Linden St, Ashvale NSW</div></div>
    <div class="proj" style="left:107px;top:59px"><div class="proj-img" role="img" aria-label="Render of a residential development"></div><div class="proj-cap">31-35 Garnet St, Ashvale NSW</div></div>
    <div class="proj" style="left:145px;top:59px"><div class="proj-img" role="img" aria-label="Render of a high-rise tower"></div><div class="proj-cap">18 Pike Rd, Elmstead NSW</div></div>
    <div class="proj" style="left:31px;top:106px"><div class="proj-img" role="img" aria-label="Render of a curved white apartment building"></div><div class="proj-cap">65-69 Reed Rd, Hollins NSW</div></div>
    <div class="proj" style="left:69px;top:106px"><div class="proj-img" role="img" aria-label="Render of an apartment block at dusk"></div><div class="proj-cap">4 Wren St, Tallow Creek NSW</div></div>
    <div class="proj" style="left:107px;top:106px"><div class="proj-img" role="img" aria-label="Render of a glass office tower"></div><div class="proj-cap">120 Harbour St, Milbrook NSW</div></div>
    <div class="proj" style="left:145px;top:106px"><div class="proj-img" role="img" aria-label="Render of a large residential block"></div><div class="proj-cap">260 Station Pde, Kellmore NSW</div></div>
    <div class="proj" style="left:31px;top:153px"><div class="proj-img" role="img" aria-label="Render of a low-rise apartment building"></div><div class="proj-cap">115 Maple St, Coralton NSW</div></div>
    <div class="proj" style="left:69px;top:153px"><div class="proj-img" role="img" aria-label="Render of a balconied apartment block"></div><div class="proj-cap">Ferndale NSW</div></div>
    <div class="proj" style="left:107px;top:153px"><div class="proj-img" role="img" aria-label="Render of a residential tower"></div><div class="proj-cap">11-17 Station Pde, Coralton NSW</div></div>
    <div class="proj" style="left:145px;top:153px"><div class="proj-img" role="img" aria-label="Render of a street-front building"></div><div class="proj-cap">640 Kings Hwy, Brightmoor NSW</div></div>
    <div class="proj" style="left:31px;top:200px"><div class="proj-img" role="img" aria-label="Render of a glass residential tower"></div><div class="proj-cap">25 Ashford St, Milbrook NSW</div></div>
    <div class="proj" style="left:69px;top:200px"><div class="proj-img" role="img" aria-label="Render of an apartment complex"></div><div class="proj-cap">410-418 Vine Rd, Greyfield NSW</div></div>
    <div class="proj" style="left:107px;top:200px"><div class="proj-img" role="img" aria-label="Render of a mid-rise building"></div><div class="proj-cap">40-46 Morrow St, Lowbank NSW</div></div>
  </section>

  <!-- Contact -->
  <section class="page col-2 row-4">
    <div class="backdrop" role="img" aria-label="Deep red low-poly backdrop" style="clip-path:polygon(0 190px,40px 160px,80px 172px,120px 195px,160px 182px,190px 162px,190px 268px,0 268px)"></div>
    <div class="vtitle">CONTACT US</div>
    <p class="contact-lead" style="top:41px">Whether it be helping you find workers, or helping you find a job, we're just a phone call away from helping you out with your needs.</p>
    <p class="contact-lead em" style="top:64px">Our friendly staff members will run you through the process of either positioning you on a jobsite or finding you the perfect candidate as an employer.</p>
    <div class="contact-row" style="top:89px">Unit 4 / 27 Forge Street, Milbrook NSW 2199 <span class="dot"><svg width="5" height="5" viewBox="0 0 5 5" fill="#fff"><path d="M2.5 .3L4.7 2.3H4v2.4H1V2.3H.3z"/></svg></span></div>
    <div class="contact-row" style="top:103px">1300 555 018,&nbsp;&nbsp;&nbsp;&nbsp;(02) 5550 1942 <span class="dot"><svg width="5" height="5" viewBox="0 0 5 5" fill="none" stroke="#fff" stroke-width=".6"><path d="M1 .8c-.5 1.6.8 3.2 2.6 3.5l.6-.9-1-.7-.5.4C2 2.7 1.6 2.2 1.5 1.6l.5-.4-.5-1z"/></svg></span></div>
    <div class="contact-row" style="top:117px">admin@ironbarklabour.com.au <span class="dot"><svg width="5" height="5" viewBox="0 0 5 5" fill="none" stroke="#fff" stroke-width=".5"><rect x=".5" y="1" width="4" height="3"/><path d="M.5 1l2 1.6 2-1.6"/></svg></span></div>
    <div class="url">www.ironbarklabour.com.au</div>
  </section>

  <!-- Back cover -->
  <section class="page col-3 row-4">
    <div class="photo dark" role="img" aria-label="Red-toned photo of a worker in a company shirt guiding a steel beam hanging from a crane" style="clip-path:polygon(0 0,190px 0,190px 150px,150px 175px,100px 168px,55px 190px,0 180px)"></div>
    <div class="backdrop" role="img" aria-label="Deep red low-poly backdrop" style="clip-path:polygon(0 180px,55px 190px,100px 168px,150px 175px,190px 150px,190px 268px,0 268px)"></div>
    <div class="brand reverse" style="left:73px;top:216px"><span class="brand-mark"></span><span class="brand-name">ironbark</span></div>
    <div class="brand-tag reverse" style="left:83px;top:234px">LABOUR HIRE SOLUTIONS</div>
    <div class="url">www.ironbarklabour.com.au</div>
  </section>

</main>
</body>
</html>
```